Covid19 Poster for workplaces

Create a poster on how to protect yourself from Corona virus at work.
We are a Staff Vitality company. We have just re-branded so we need to fit in with our brand. We like clean and fresh, slightly amusing is ok if it will draw attention but it's an important topic. A4 and A3 please.

Content:

Headline: Lower the risk of COVID 19 in the workplace.

BE WELL

Bring your own cup - don’t share cups and food.
Elbow tap instead of handshakes and kisses
Wash your hands often - with soap.
Elbow or tissues when you cough or sneeze then straight in the bin
Leave your face alone after touching shared surfaces
Leave your bugs at home if you’re feeling unwell.

Call health line if you have a cough, a high temperature and shortness of breath. 0800 472 9160

Based on recommendations from ZPK and QLN

Target Market(s)

Employees - so anyone

Other font styles liked:
• Use the closest font to the brand documents

Requirements
Should not have
• Clip art

```html
<!DOCTYPE html>
<html lang="en">
<head>
<meta charset="utf-8">
<title>Lower the risk of COVID 19 in the workplace – Poster</title>
<link href="https://fonts.googleapis.com/css2?family=Montserrat:wght@600;700;800;900&family=Roboto+Condensed:wght@700&display=swap" rel="stylesheet">
<style>
  :root{
    --teal:#1fa6ae;
    --teal-dark:#17868d;
    --ink:#1d2c30;
    --black:#0b0b0b;
    --red:#e8201c;
    --panel:#f1f2f2;
    --footer:#1a2b2d;
    --white:#ffffff;
    --bg:#eeeeec;
  }
  *{box-sizing:border-box;margin:0;padding:0}
  html,body{width:1200px;height:1200px;overflow:hidden;background:var(--bg)}
  .poster{
    position:absolute;left:197px;top:30px;width:806px;height:1140px;
    background:var(--white);overflow:hidden;
    box-shadow:0 6px 18px rgba(0,0,0,.18);
    font-family:"Montserrat",sans-serif;
  }
  .hero{position:absolute;left:0;top:0;width:806px;height:518px;background:var(--teal)}
  .brand{position:absolute;left:39px;top:52px;display:flex;align-items:center;gap:12px}
  .brand-dot{width:34px;height:34px;border-radius:50%;background:var(--white)}
  .brand-name{font-family:"Montserrat",sans-serif;font-weight:700;font-size:25px;line-height:25px;color:var(--white);width:150px}
  .hero-photo{
    position:absolute;left:243px;top:113px;width:529px;height:228px;border-radius:28px;
    background:linear-gradient(120deg,#2b3a3e 0%,#3f5558 40%,#7a6a55 65%,#2a3b3c 100%);
  }
  .headline{position:absolute;left:41px;top:358px;font-weight:800;color:var(--ink);line-height:48px}
  .headline .line{display:block;font-size:41px}
  .headline .hl{color:var(--white)}
  .headline .big{font-size:52px;color:var(--white);font-weight:900;line-height:56px}
  .be-well{
    position:absolute;left:0;top:530px;width:806px;text-align:center;
    font-weight:900;font-size:82px;letter-spacing:-2px;color:var(--black);line-height:86px;
  }
  .box{position:absolute;left:28px;width:760px;border:2px solid;border-radius:14px;background:var(--panel)}
  .box-dos{top:659px;height:216px;border-color:var(--teal)}
  .box-donts{top:917px;height:160px;border-color:var(--red)}
  .pill{
    position:absolute;left:50%;transform:translateX(-50%);height:52px;border-radius:14px;
    display:flex;align-items:center;justify-content:center;gap:8px;
    color:var(--white);font-weight:800;font-size:37px;
  }
  .pill-dos{top:631px;width:178px;background:var(--teal)}
  .pill-donts{top:886px;width:232px;background:var(--red)}
  .pill svg{width:38px;height:38px}
  .item{position:absolute;display:flex;align-items:center;gap:14px;
    font-family:"Roboto Condensed",sans-serif;font-weight:700;font-size:17px;line-height:17px;color:var(--black)}
  .item svg{flex:none;width:52px;height:52px}
  .footer{position:absolute;left:0;top:1020px;width:806px;height:120px;background:var(--footer);
    text-align:center;color:var(--white)}
  .footer-call{margin-top:20px;font-weight:700;font-size:20.5px;line-height:26px}
  .footer-call .phone{color:var(--teal)}
  .footer-call svg{width:17px;height:17px;vertical-align:-2px}
  .footer-note{margin-top:9px;font-size:11px;font-weight:600}
</style>
</head>
<body>
<div class="poster">
  <section class="hero">
    <div class="brand">
      <span class="brand-dot"></span>
      <span class="brand-name">Staff Vitality</span>
    </div>
    <div class="hero-photo" role="img" aria-label="Photo of smiling colleagues chatting at their office desks"></div>
    <h1 class="headline">
      <span class="line">Lower the risk</span>
      <span class="line">of <span class="hl">COVID 19</span> in the</span>
      <span class="line big">WORKPLACE</span>
    </h1>
  </section>

  <h2 class="be-well">BE WELL</h2>

  <div class="box box-dos"></div>
  <div class="pill pill-dos">
    <svg viewBox="0 0 40 40"><circle cx="20" cy="20" r="17" fill="none" stroke="#fff" stroke-width="2.5"/><path d="M12 20.5l5.5 5.5L28 14.5" fill="none" stroke="#fff" stroke-width="3" stroke-linecap="round" stroke-linejoin="round"/></svg>
    DO’S
  </div>

  <div class="item" style="left:46px;top:702px">
    <svg viewBox="0 0 52 52"><rect x="4" y="12" width="32" height="30" rx="5" fill="var(--teal)"/><path d="M36 18h5a6 6 0 0 1 0 12h-5" fill="none" stroke="var(--teal)" stroke-width="5"/></svg>
    <span>Bring your<br>own cup</span>
  </div>
  <div class="item" style="left:304px;top:702px">
    <svg viewBox="0 0 52 52"><path d="M8 4h9v30h28a6 6 0 0 1 0 12H14a6 6 0 0 1-6-6z" fill="var(--teal)"/></svg>
    <span>Elbow tap</span>
  </div>
  <div class="item" style="left:540px;top:702px">
    <svg viewBox="0 0 52 52"><rect x="4" y="22" width="30" height="24" rx="6" fill="var(--teal)"/><rect x="20" y="26" width="26" height="5" rx="2.5" fill="var(--teal)"/><rect x="20" y="34" width="26" height="5" rx="2.5" fill="var(--teal)"/><circle cx="36" cy="8" r="4" fill="var(--teal)"/><circle cx="45" cy="14" r="3" fill="var(--teal)"/><circle cx="28" cy="12" r="3" fill="var(--teal)"/></svg>
    <span>Wash your hands<br>often - with soap.</span>
  </div>

  <div class="item" style="left:46px;top:784px">
    <svg viewBox="0 0 52 52"><path d="M4 22h22l-3 26H7z" fill="var(--teal)"/><rect x="2" y="17" width="26" height="4" rx="2" fill="var(--teal)"/><circle cx="42" cy="8" r="5" fill="var(--teal)"/><rect x="36" y="15" width="12" height="20" rx="4" fill="var(--teal)"/><rect x="37" y="33" width="4" height="16" fill="var(--teal)"/><rect x="43" y="33" width="4" height="16" fill="var(--teal)"/></svg>
    <span>Elbow or tissues<br>when you cough<br>or sneeze then<br>straight in the bin</span>
  </div>
  <div class="item" style="left:304px;top:784px">
    <svg viewBox="0 0 52 52"><circle cx="26" cy="24" r="20" fill="var(--teal)"/><rect x="18" y="38" width="16" height="12" fill="var(--teal)"/></svg>
    <span>Leave your face<br>alone after touching<br>shared surfaces</span>
  </div>
  <div class="item" style="left:540px;top:784px">
    <svg viewBox="0 0 52 52"><path d="M18 18v-6a8 8 0 0 1 16 0v6" fill="none" stroke="var(--teal)" stroke-width="4"/><path d="M8 18h36l3 30H5z" fill="none" stroke="var(--teal)" stroke-width="4" stroke-linejoin="round"/></svg>
    <span>Leave your bugs<br>at home if you’re<br>feeling unwell.</span>
  </div>

  <div class="box box-donts"></div>
  <div class="pill pill-donts">
    <svg viewBox="0 0 40 40"><circle cx="20" cy="20" r="18" fill="#fff"/><path d="M14 14l12 12M26 14L14 26" stroke="var(--red)" stroke-width="3.5" stroke-linecap="round"/></svg>
    DON’TS
  </div>

  <div class="item" style="left:56px;top:956px">
    <svg viewBox="0 0 52 52" style="width:60px"><path d="M2 16h12c8 0 14-6 24-6 6 0 12 2 12 6s-6 6-12 6v16H2z" fill="var(--red)"/></svg>
    <span>Don’t share cups and food.</span>
  </div>
  <div class="item" style="left:432px;top:952px">
    <svg viewBox="0 0 64 52" style="width:66px"><path d="M2 8l12 6-4 18-8-4z" fill="var(--red)"/><path d="M62 8l-12 6 4 18 8-4z" fill="var(--red)"/><path d="M16 14l12-2 8 4 12-2 4 16-14 12c-3 2-6 1-8-1l-14-11z" fill="var(--red)"/></svg>
    <span>Don’t do handshakes and kisses</span>
  </div>

  <footer class="footer">
    <p class="footer-call">Call health line if you have a cough, a high temperature and<br>shortness of breath
      <svg viewBox="0 0 20 20"><circle cx="10" cy="10" r="8.5" fill="none" stroke="#fff" stroke-width="1.5"/><path d="M7 5.5l1.6 2.4-1 1.2a6 6 0 0 0 3.3 3.3l1.2-1 2.4 1.6-.8 1.6c-4 .4-8.6-4.2-8.2-8.2z" fill="#fff"/></svg>
      <span class="phone">0800 472 9160</span></p>
    <p class="footer-note">Based on recommendations from ZPK and QLN</p>
  </footer>
</div>
</body>
</html>
```